CREATE A BUSINESS CARD FOR A BOAT CLEANING SERVICE

WE ARE STARTING A NEW BOAT CLEANING BUSINESS. WE DIVE UNDERWATER TO CLEAN BOAT HULLS, JETTIES, UNDERWATER STRUCTURES ETC. WE ARE LOOKING FOR AN UPPERMARKET MODERN LOGO AND BUSINESS CARD AS ALOT OF OUR TARGET MARKET WILL BE HIGH END. YOU HAVE TO DESIGN A BUSINESS CARD AND LOGO SEPERATELY .
THE BUSINESS CARD DIMESNION MUST BE STANDARD SIZE.
The standard dimensions of a printed business card are 3.5 x 2 inches

Target Market(s)

UNDERWATER SERVICED

Industry/Entity Type

Business

Contact Information for Business Card

HALDEN UNDERWATER SERVICES

Font styles to use
Serif

Colors

Designer to choose colors to be used in the design.

Requirements
Must have
• HALDEN
Nice to have
• dark
Should not have
• more than 3 colors

```html
<!DOCTYPE html>
<html lang="en">
<head>
<meta charset="utf-8">
<title>Halden Underwater Services – Business Card</title>
<link rel="stylesheet" href="https://fonts.googleapis.com/css2?family=Open+Sans:wght@400;600;700&display=swap">
<style>
  :root {
    --backdrop: #545454;
    --card-white: #ffffff;
    --brand-blue: #17508a;
    --brand-grey: #7b7b7b;
    --ink: #1a1a1a;
    --rule: #8a8fa8;
  }
  * { margin: 0; padding: 0; box-sizing: border-box; }
  html, body {
    width: 1200px; height: 900px; overflow: hidden;
    background: var(--backdrop);
    font-family: "Open Sans", Arial, sans-serif;
  }
  .stage { position: relative; width: 1200px; height: 900px; }
  .card {
    position: absolute; top: 170px;
    width: 347px; height: 561px;
    box-shadow: 3px 3px 6px rgba(0,0,0,0.45);
  }
  .card--front { left: 259px; background: var(--card-white); text-align: center; }
  .card--back { left: 631px; background: var(--brand-blue); }

  .brand { position: absolute; left: 0; right: 0; top: 250px; color: var(--brand-blue); font-weight: 600; }
  .brand__mark {
    display: block; width: 14px; height: 14px; border-radius: 50%;
    background: var(--brand-blue); margin: -120px auto 0;
  }
  .brand__name { display: block; margin-top: 88px; font-size: 54px; line-height: 1; letter-spacing: 1px; }
  .brand__tagline { display: block; margin-top: 4px; font-size: 14px; letter-spacing: 3.4px; }

  .contact { position: absolute; left: 0; right: 0; top: 340px; color: var(--ink); }
  .contact__name { font-size: 21px; font-weight: 600; color: var(--brand-blue); line-height: 1.2; }
  .contact__role { font-size: 14.5px; line-height: 1.4; }
  .contact__rule { width: 146px; height: 1px; background: var(--rule); margin: 12px auto 10px; }
  .contact__line { font-size: 14.5px; line-height: 21px; }
  .contact__label { color: var(--brand-blue); font-weight: 600; }
  .contact__web { color: var(--brand-blue); font-weight: 600; }
  .contact__address { font-size: 14.5px; line-height: 17.5px; margin-top: -2px; }

  .slogan {
    position: absolute; left: 0; right: 0; top: 186px;
    text-align: center; color: var(--card-white);
    font-size: 26.5px; font-weight: 600; line-height: 51px; letter-spacing: 0.3px;
  }
</style>
</head>
<body>
<main class="stage">
  <section class="card card--front" aria-label="Business card front">
    <div class="brand">
      <span class="brand__mark" aria-hidden="true"></span>
      <span class="brand__name">HALDEN</span>
      <span class="brand__tagline">UNDERWATER SERVICES</span>
    </div>
    <div class="contact">
      <p class="contact__name">MARA QUINLAN</p>
      <p class="contact__role">Managing Director</p>
      <div class="contact__rule"></div>
      <p class="contact__line"><span class="contact__label">P:</span> 555-218-4630</p>
      <p class="contact__line"><span class="contact__label">E:</span> hello@haldendive.com</p>
      <p class="contact__line contact__web">www.haldendive.com</p>
      <div class="contact__rule"></div>
      <p class="contact__address">48 Harbour Quay Road<br>Port Ellis, 204518</p>
    </div>
  </section>

  <section class="card card--back" aria-label="Business card back">
    <p class="slogan">WE DIVE UNDERWATER<br>TO CLEAN BOAT,HULLS<br>JETTIES, UNDERWATER<br>STRUCTURES ETC</p>
  </section>
</main>
</body>
</html>
```